Redesign current business card for food company

i would like to redesign my business card. our company is food company, our product range from chips, juices, milk and etc (mostly dried food stuff).
I want o keep same logo but , the rest is open to new design.
you can check at our website about our company www.torvikeats.com

Target Market(s)

most of food company

Industry/Entity Type

Business

Contact Information for Business Card

I want to keep more to blue color...

Colors
3176b5
abd036

Requirements
Must have
• our old logo
Nice to have
• we do not mind to have nice material on bus card in order to accomplish nice design. for example: using spot uv, embossed and etc.

```html
<!DOCTYPE html>
<html lang="en">
<head>
<meta charset="utf-8">
<title>Torvik Business Card</title>
<link href="https://fonts.googleapis.com/css2?family=Roboto:wght@400;500;700&display=swap" rel="stylesheet">
<style>
  :root {
    --brand-blue: #3176b5;
    --sky-blue: #4aa8d8;
    --deep-blue: #2a64a8;
    --logo-blue: #2b5fc0;
    --lime: #abd036;
    --paper: #ffffff;
    --paper-shade: #eeeeee;
    --backdrop: #e4e6e9;
  }
  * { margin: 0; padding: 0; box-sizing: border-box; }
  html, body { width: 1200px; height: 1023px; overflow: hidden; }
  body {
    background: var(--backdrop);
    font-family: "Roboto", Arial, sans-serif;
    position: relative;
  }
  .card {
    position: absolute;
    left: 250px;
    width: 700px;
    height: 400px;
    border-radius: 18px;
    overflow: hidden;
    box-shadow: 0 6px 18px rgba(0,0,0,0.18);
  }
  .card-front { top: 70px; background: radial-gradient(circle at 60% 25%, var(--paper) 40%, var(--paper-shade) 100%); }
  .card-back {
    top: 550px;
    background: linear-gradient(135deg, var(--deep-blue) 0%, var(--brand-blue) 45%, var(--sky-blue) 100%);
    display: flex; align-items: center; justify-content: center;
  }
  .front-art { position: absolute; inset: 0; }
  .logo-word {
    position: absolute;
    left: 380px; top: 24px;
    font-size: 64px; font-weight: 700;
    color: var(--logo-blue);
    letter-spacing: -1px;
  }
  .website {
    position: absolute;
    right: 26px; top: 150px;
    font-size: 13px; color: var(--lime);
    letter-spacing: 0.5px;
  }
  .holder { position: absolute; left: 40px; top: 168px; color: var(--paper); }
  .holder-name { font-size: 29px; font-weight: 500; white-space: nowrap; }
  .holder-title { font-size: 16px; color: var(--lime); margin-top: 2px; }
  .contact-list { position: absolute; left: 40px; top: 242px; list-style: none; }
  .contact-item {
    display: flex; align-items: center; gap: 12px;
    height: 29px; font-size: 15px; color: var(--paper);
    white-space: nowrap;
  }
  .contact-icon {
    width: 22px; height: 22px;
    border: 1.5px solid var(--lime);
    border-radius: 50%;
    display: flex; align-items: center; justify-content: center;
    flex: none;
  }
  .contact-icon svg { width: 12px; height: 12px; fill: var(--paper); }
  .back-word { font-size: 150px; font-weight: 700; color: var(--paper); letter-spacing: -3px; }
</style>
</head>
<body>
  <section class="card card-front">
    <svg class="front-art" viewBox="0 0 700 400" width="700" height="400">
      <defs>
        <linearGradient id="frontBlue" x1="0" y1="1" x2="1" y2="0">
          <stop offset="0" stop-color="#2f78b8"/>
          <stop offset="1" stop-color="#4aaedc"/>
        </linearGradient>
      </defs>
      <path d="M0,100 C200,128 420,186 640,192" fill="none" stroke="var(--lime)" stroke-width="6"/>
      <path d="M0,114 C220,144 450,204 700,198 L700,400 L0,400 Z" fill="url(#frontBlue)"/>
    </svg>

    <div class="logo-word">torvik</div>
    <div class="website">www.torvikeats.com</div>

    <div class="holder">
      <div class="holder-name">Marcus Delavane</div>
      <div class="holder-title">President</div>
    </div>

    <ul class="contact-list">
      <li class="contact-item">
        <span class="contact-icon"><svg viewBox="0 0 12 12"><path d="M2.5 1 L4.5 1 L5 3.5 L3.8 4.5 C4.5 6 6 7.5 7.5 8.2 L8.5 7 L11 7.5 L11 9.5 C11 10.3 10.3 11 9.5 11 C5 11 1 7 1 2.5 C1 1.7 1.7 1 2.5 1Z"/></svg></span>
        555 204 1988
      </li>
      <li class="contact-item">
        <span class="contact-icon"><svg viewBox="0 0 12 12"><path d="M3.5 0.5 H8.5 A1 1 0 0 1 9.5 1.5 V10.5 A1 1 0 0 1 8.5 11.5 H3.5 A1 1 0 0 1 2.5 10.5 V1.5 A1 1 0 0 1 3.5 0.5Z M3.8 2 V9 H8.2 V2Z"/></svg></span>
        555 318 6567
      </li>
      <li class="contact-item">
        <span class="contact-icon"><svg viewBox="0 0 12 12"><path d="M3 1 H8 V4 H3Z M1 5 H11 V11 H1Z M3 7 H5 V8 H3Z M7 7 H9 V8 H7Z M3 9 H5 V10 H3Z M7 9 H9 V10 H7Z"/></svg></span>
        555 204 1977
      </li>
      <li class="contact-item">
        <span class="contact-icon"><svg viewBox="0 0 12 12"><path d="M1 2.5 H11 V9.5 H1Z M1.5 3 L6 6.5 L10.5 3" stroke="var(--brand-blue)" stroke-width="0.8"/></svg></span>
        Marcus@torvikeats.com
      </li>
      <li class="contact-item">
        <span class="contact-icon"><svg viewBox="0 0 12 12"><path d="M6 0.8 C3.8 0.8 2.3 2.4 2.3 4.4 C2.3 7 6 11.2 6 11.2 C6 11.2 9.7 7 9.7 4.4 C9.7 2.4 8.2 0.8 6 0.8Z M6 3 A1.4 1.4 0 1 0 6.01 3Z"/></svg></span>
        2418 W Alder St. Fairmont CA 90412
      </li>
    </ul>
  </section>

  <section class="card card-back">
    <div class="back-word">torvik</div>
  </section>
</body>
</html>
```